Wedding location search & compare

We need a web design for a website (mobile & pc) which allows for searching and comparing of wedding locations. The design should be clean, stylish and original and it should have the following functionality:
- a search function (with summary overview and map view)
- a comparing function
- detail page per location
- review possibility
- login for storing favorites and show own history
- social function (liking, sharing, send to and cavorting)
- ad placement
- contact form

We also require a Logo Design. Please submit your ideas for that project here: Logo Design needed for web design project.

```html
<!DOCTYPE html>
<html lang="en">
<head>
<meta charset="utf-8">
<title>Wedding Locations – Compare &amp; Search</title>
<link href="https://fonts.googleapis.com/css2?family=Didact+Gothic&family=Open+Sans:wght@400;600;700&display=swap" rel="stylesheet">
<style>
:root{
  --red:#d23a3f;
  --red-dark:#b92e33;
  --orange:#e0874f;
  --rust:#c4653b;
  --ink:#333;
  --muted:#8a8a8a;
  --line:#dcdcdc;
  --paper:#fff;
  --field:#fff;
  --plum:#6e2c79;
}
*{box-sizing:border-box;margin:0;padding:0}
html,body{width:1200px;height:2171px;overflow:hidden}
body{position:relative;background:linear-gradient(#e9e9e9,#f4f4f4 480px,#fff 620px);font-family:"Open Sans",sans-serif;color:var(--ink)}
.abs{position:absolute}
.heading{font-family:"Didact Gothic",sans-serif;font-weight:400}

/* header */
.login-field{top:16px;height:23px;border-radius:12px;background:var(--field);border:1px solid #ddd;font-size:10px;color:#666;padding:5px 12px}
.login-btn{top:16px;left:997px;width:60px;height:23px;border-radius:12px;background:var(--orange);color:#fff;font-size:11px;text-align:center;line-height:23px}
.brand{left:130px;top:44px;display:flex;align-items:center;gap:12px}
.brand-dot{width:26px;height:26px;border-radius:50%;background:var(--red)}
.brand-name{font-family:"Didact Gothic",sans-serif;font-size:36px;color:var(--red);line-height:1}
.brand-tag{left:218px;top:86px;font-family:"Didact Gothic",sans-serif;font-size:16px;color:#444;letter-spacing:.5px}
.support{left:900px;top:64px;width:157px;text-align:right;font-size:16px;color:var(--red);font-family:"Didact Gothic",sans-serif}
.phone{left:890px;top:86px;width:167px;display:flex;align-items:center;justify-content:flex-end;gap:8px;font-family:"Didact Gothic",sans-serif;font-size:23px;color:#333}

/* nav */
.ribbon{top:145px}
.nav{left:130px;top:126px;width:940px;height:51px;background:linear-gradient(#dc474b,#c6343a);display:flex;justify-content:space-around;align-items:center;padding:0 14px;box-shadow:0 2px 4px rgba(0,0,0,.2)}
.nav a{color:#fff;text-decoration:none;font-family:"Didact Gothic",sans-serif;font-size:17px}

/* hero */
.hero{left:130px;top:177px;width:940px;height:448px;background:linear-gradient(#b9d3e6 0%,#dce8ef 24%,#8db3c7 28%,#6f9a55 44%,#74a834 70%,#5f8d25 100%)}
.searchbar{left:130px;top:550px;width:940px;height:75px;background:rgba(90,70,30,.72);border-bottom:4px solid #39454f}
.search-field{top:20px;height:32px;background:#fff;font-size:11px;color:#555;padding:9px 14px}
.find-btn{left:706px;top:20px;width:175px;height:34px;background:linear-gradient(#e59a5e,#cf7a3f);color:#fff;font-family:"Didact Gothic",sans-serif;font-size:17px;text-align:center;line-height:34px}

/* content */
.overview-title{left:135px;top:656px;font-size:29px;color:#222}
.overview-text{left:135px;top:699px;width:625px;font-size:11.5px;line-height:18px;color:#444}
.overview-text p+p{margin-top:5px}
.section-title{font-size:23px;color:var(--rust)}
.plain-title{font-size:24px;color:#333}
.photo{display:block}
.compare-card{width:300px;height:122px}
.compare-card .photo{position:absolute;left:0;top:0;width:133px;height:122px}
.compare-card h3{position:absolute;left:147px;top:0;font-family:"Didact Gothic",sans-serif;font-weight:400;font-size:17px;color:#333}
.compare-card p{position:absolute;left:147px;top:26px;width:150px;font-size:10.5px;line-height:18px;color:var(--muted)}
.read-link{position:absolute;left:147px;top:100px;font-size:11.5px;color:var(--red)}
.divider{left:130px;top:1213px;width:634px;height:1px;background:var(--line)}

.tile{width:196px}
.tile .photo{width:196px;height:99px}
.tile h3{font-family:"Didact Gothic",sans-serif;font-weight:400;font-size:17px;color:#333;margin-top:14px}
.tile p{font-size:10.5px;line-height:17px;color:var(--muted);margin-top:4px}
.btn-small{display:inline-block;margin-top:14px;width:80px;height:24px;background:linear-gradient(#dd4b4f,#c3353a);color:#fff;font-size:11px;text-align:center;line-height:24px;border-radius:2px}

/* sidebar */
.panel{left:790px;width:280px;background:#fff;border:1px solid #ddd}
.panel-head{height:46px;padding:12px 22px;font-family:"Didact Gothic",sans-serif;font-size:20px}
.contact .panel-head{background:linear-gradient(#fafafa,#eee);border-bottom:1px solid #ddd;color:#444}
.form-field{position:absolute;left:20px;width:234px;height:32px;border:1px solid #d5d5d5;border-radius:3px;font-size:10px;color:#888;padding:9px 12px}
.submit{position:absolute;left:20px;top:252px;width:88px;height:30px;background:linear-gradient(#dc474b,#c6343a);color:#fff;font-size:14px;text-align:center;line-height:30px;border-radius:2px}
.posts .panel-head{background:linear-gradient(#d27744,#b9582f);color:#fff}
.post{padding:0 22px;margin-top:14px;font-size:10.5px;line-height:18px;color:#666}
.post strong{font-weight:400;font-size:12px;color:#444}
.post time{display:block;color:#333;margin-top:4px}
.map{left:790px;top:1209px;width:280px;height:231px;background:linear-gradient(135deg,#e8e6dc,#dfe4d9 55%,#cfdbe4)}
.map-band{left:790px;top:1394px;width:280px;height:46px;background:rgba(110,60,35,.88);color:#fff;font-family:"Didact Gothic",sans-serif;font-size:20px;padding:10px 24px}
.ad{left:790px;top:1459px;width:280px;height:232px;background:linear-gradient(#eceff4,#dde2ea 55%,#7b5a6e 62%,#4b2f46)}
.ad-lead{left:806px;top:1521px;font-size:12.5px;color:#333}
.ad-title{left:806px;top:1540px;font-weight:700;font-size:20px;color:#6a2a78}
.ad-cta{left:806px;top:1576px;height:22px;padding:0 12px;background:#7a3a86;color:#fff;font-size:11px;font-weight:700;line-height:22px;border-radius:3px}
.ad-foot{left:790px;top:1664px;width:280px;height:27px;background:var(--plum);color:#fff;font-size:9.5px;letter-spacing:1px;padding:7px 16px}

/* footer */
.main-sheet{left:0;top:470px;width:1200px;height:1397px;background:#fff;z-index:-1}
.footer{left:0;top:1867px;width:1200px;height:247px;background:linear-gradient(#e4e4e4,#ececec)}
.foot-col{top:1903px}
.foot-col h4{font-family:"Didact Gothic",sans-serif;font-weight:400;font-size:19px;color:var(--red);margin-bottom:8px}
.foot-col li{list-style:none;font-size:11.5px;color:#555;line-height:25.6px}
.social{left:840px;top:1937px;display:flex;gap:7px}
.social span{width:25px;height:25px;border-radius:50%;background:var(--red);display:block}
.copyright{left:138px;top:2134px;font-size:11px;color:#666}
</style>
</head>
<body>
<div class="abs main-sheet"></div>

<!-- header -->
<div class="abs login-field" style="left:745px;width:121px">Username</div>
<div class="abs login-field" style="left:871px;width:121px">Password</div>
<div class="abs login-btn">Login</div>

<div class="abs brand"><span class="brand-dot"></span><span class="brand-name">Wedding Locations</span></div>
<div class="abs brand-tag">Compare &amp; Search</div>

<div class="abs support">24/7 Support</div>
<div class="abs phone">
  <svg width="26" height="26" viewBox="0 0 26 26"><circle cx="13" cy="13" r="11.5" fill="none" stroke="#d23a3f" stroke-width="2"/><path d="M9 7.5c1-.6 1.7.1 2.2 1.2l.8 1.8c.3.8-.5 1.3-1 1.8.7 1.5 1.9 2.7 3.4 3.4.5-.5 1-1.3 1.8-1l1.8.8c1.1.5 1.8 1.2 1.2 2.2-.9 1.4-2.4 1.8-4 1.1-3.2-1.4-5.600-3.8-7-7-.7-1.600-.3-3.100 1.100-4z" fill="#d23a3f"/></svg>
  <span>555.204.3187</span>
</div>

<!-- nav -->
<svg class="abs ribbon" style="left:72px" width="60" height="56" viewBox="0 0 60 56"><path d="M0 0H60V56H0L16 28Z" fill="#b92e33"/></svg>
<svg class="abs ribbon" style="left:1068px" width="60" height="56" viewBox="0 0 60 56"><path d="M60 0H0V56H60L44 28Z" fill="#b92e33"/></svg>
<nav class="abs nav">
  <a href="#">About Us</a><a href="#">Venues</a><a href="#">Locations</a><a href="#">Book Now</a><a href="#">Special Offers</a><a href="#">Reviews</a><a href="#">Blog</a><a href="#">Contact</a>
</nav>

<!-- hero -->
<div class="abs hero" role="img" aria-label="Outdoor wedding ceremony on a green lawn by the sea, white chairs lining a flower-strewn aisle to an arch"></div>
<div class="abs searchbar">
  <div class="abs search-field" style="left:69px;width:226px">Cermony &amp; Reception Venue</div>
  <div class="abs search-field" style="left:322px;width:183px">Overview</div>
  <div class="abs search-field" style="left:512px;width:182px">Map
    <svg style="position:absolute;right:10px;top:9px" width="12" height="14" viewBox="0 0 12 14"><path d="M6 0a5 5 0 0 1 5 5c0 3.5-5 9-5 9S1 8.5 1 5a5 5 0 0 1 5-5z" fill="#999"/><circle cx="6" cy="5" r="2" fill="#fff"/></svg>
  </div>
  <div class="abs find-btn">Find Vendors</div>
</div>

<!-- overview -->
<h1 class="abs heading overview-title">Wedding Locations Overview</h1>
<div class="abs overview-text">
  <p>Vivamus porttitor purus nisi eleifend libero a tempus libero lectus feugiat felis Morbi diam mauris viverra in gravida eu mattis in ante Morbi eget arcu Morbi porta libero id ullamcorper nonummy nibh ligula pulvinar metus eget consectetuer augue nisi quis lacus Ut ac mi quis lacus mollis aliquam</p>
  <p>Curabitur iaculis tempus eros Curabitur vel mi sit amet malesuada ultrices Ut nisi erat fermentum vel congue id euismod in elit Fusce ultricies orci ac feugiat suscipit leo massa sodales velit et scelerisqu</p>
</div>

<h2 class="abs heading section-title" style="left:135px;top:831px">Browse Venues by Comparing</h2>

<article class="abs compare-card" style="left:135px;top:880px">
  <div class="photo" role="img" aria-label="Banquet hall with purple chair sashes" style="background:linear-gradient(#c9a77a,#6d5a8c)"></div>
  <h3>Etiam venenatis</h3>
  <p>Cum sociis natoque penati- bus et magnis dis parturient montes nascetur ridiculus mus In iaculis facilisis ma</p>
  <span class="read-link">Read More ›</span>
</article>
<article class="abs compare-card" style="left:460px;top:880px">
  <div class="photo" role="img" aria-label="Draped marquee with round dining tables" style="background:linear-gradient(#e8d6c4,#9c7a5c)"></div>
  <h3>Vivamus porttitor</h3>
  <p>Cum sociis natoque penati- bus et magnis dis parturient montes nascetur ridiculus mus In iaculis facilisis ma</p>
  <span class="read-link">Read More ›</span>
</article>
<article class="abs compare-card" style="left:135px;top:1045px">
  <div class="photo" role="img" aria-label="Bright room with tall windows and set tables" style="background:linear-gradient(#f2ece2,#c9b9a2)"></div>
  <h3>Tempor cursus</h3>
  <p>Cum sociis natoque penati- bus et magnis dis parturient montes nascetur ridiculus mus In iaculis facilisis ma</p>
  <span class="read-link">Read More ›</span>
</article>
<article class="abs compare-card" style="left:460px;top:1045px">
  <div class="photo" role="img" aria-label="Garden reception with pink flower arrangements" style="background:linear-gradient(#d9b8c6,#5d8a3f)"></div>
  <h3>Morbi ornare</h3>
  <p>Cum sociis natoque penati- bus et magnis dis parturient montes nascetur ridiculus mus In iaculis facilisis ma</p>
  <span class="read-link">Read More ›</span>
</article>

<div class="abs divider"></div>

<!-- reviews -->
<h2 class="abs heading plain-title" style="left:130px;top:1240px">Latest Reviews</h2>
<article class="abs tile" style="left:130px;top:1284px">
  <div class="photo" role="img" aria-label="Garden ceremony with white chairs" style="background:linear-gradient(#4f7a3a,#a9b9a0)"></div>
  <h3>Wedding Venue Name</h3><p>Cum sociis natoque penatibus et magnis dis parturient montes nascetur ridiculus mus In</p><span class="btn-small">Read More</span>
</article>
<article class="abs tile" style="left:343px;top:1284px">
  <div class="photo" role="img" aria-label="Pavilion with rows of chairs facing a view" style="background:linear-gradient(#c7b49a,#8a7058)"></div>
  <h3>Wedding Venue Name</h3><p>Cum sociis natoque penatibus et magnis dis parturient montes nascetur ridiculus mus In</p><span class="btn-small">Read More</span>
</article>
<article class="abs tile" style="left:557px;top:1284px">
  <div class="photo" role="img" aria-label="Evening ballroom with round tables" style="background:linear-gradient(#5a3a2c,#c49a6c)"></div>
  <h3>Wedding Venue Name</h3><p>Cum sociis natoque penatibus et magnis dis parturient montes nascetur ridiculus mus In</p><span class="btn-small">Read More</span>
</article>

<!-- details -->
<h2 class="abs heading plain-title" style="left:130px;top:1541px">Venues Details</h2>
<article class="abs tile" style="left:132px;top:1581px">
  <div class="photo" role="img" aria-label="Hall with purple drapery" style="background:linear-gradient(#9a5aa0,#e6dce8)"></div>
  <h3>Venue Tittle</h3><p>Cum sociis natoque penatibus et magnis dis parturient montes nascetur ridiculus mus In</p><span class="btn-small">Read More</span>
</article>
<article class="abs tile" style="left:346px;top:1581px">
  <div class="photo" role="img" aria-label="Lawn with blue-clothed tables" style="background:linear-gradient(#c8d3dc,#5d8f3a)"></div>
  <h3>Venue Tittle</h3><p>Cum sociis natoque penatibus et magnis dis parturient montes nascetur ridiculus mus In</p><span class="btn-small">Read More</span>
</article>
<article class="abs tile" style="left:560px;top:1581px">
  <div class="photo" role="img" aria-label="Terrace with pink table settings" style="background:linear-gradient(#eef0f2,#d49aa2)"></div>
  <h3>Venue Tittle</h3><p>Cum sociis natoque penatibus et magnis dis parturient montes nascetur ridiculus mus In</p><span class="btn-small">Read More</span>
</article>

<!-- sidebar -->
<aside class="abs panel contact" style="top:646px;height:305px">
  <div class="panel-head">Contact Form</div>
  <div class="form-field" style="top:64px">Your Name</div>
  <div class="form-field" style="top:104px">Email address</div>
  <div class="form-field" style="top:144px">Phone</div>
  <div class="form-field" style="top:183px;height:62px">Message</div>
  <div class="submit">Submit</div>
</aside>

<aside class="abs panel posts" style="top:968px;height:219px">
  <div class="panel-head">Recent Posts</div>
  <div class="post"><strong>Dis parturient monte</strong> @ Cum sociis natoque penatibus et magnis dis parturient montes nascetur ridiculus mus iaculis<time>2 hours ago</time></div>
  <div class="post"><strong>Morbi diam mauris</strong> @ Cum sociis natoque penatibus et magnis dis part<time>2 hours ago</time></div>
</aside>

<div class="abs map" role="img" aria-label="Road map showing venue locations"></div>
<div class="abs map-band">Venues by Map View</div>

<div class="abs ad" role="img" aria-label="Advertisement: overwater bungalows at sunset"></div>
<div class="abs ad-lead">Uncover your next destination with</div>
<div class="abs ad-title">WANDER DESK</div>
<div class="abs ad-cta">GET STARTED ›</div>
<div class="abs ad-foot">WANDER DESK JOURNEYS</div>

<!-- footer -->
<footer class="abs footer"></footer>
<div class="abs foot-col" style="left:138px"><h4>Quick Links</h4><ul><li>Natoque penatibus</li><li>Et magnis</li><li>Dis parturient</li><li>Montes nascetur</li><li>Ridiculus mus In</li></ul></div>
<div class="abs foot-col" style="left:317px"><h4>Best Venues</h4><ul><li>Etiam est nunc</li><li>Venenatis</li><li>Tristique eu</li><li>Imperdiet ac nisl</li><li>Cum sociis</li></ul></div>
<div class="abs foot-col" style="left:501px"><h4>Resources</h4><ul><li>Natoque penatibus</li><li>Et magnis</li><li>Dis parturient</li><li>Montes nascetur</li><li>Ridiculus mus In</li></ul></div>
<div class="abs foot-col" style="left:672px"><h4>Support</h4><ul><li>Natoque penatibus</li><li>Et magnis</li><li>Dis parturient</li><li>Montes nascetur</li><li>Ridiculus mus In</li></ul></div>
<div class="abs foot-col" style="left:838px"><h4>Get in touch</h4></div>
<div class="abs social"><span></span><span></span><span></span><span></span><span></span></div>

<div class="abs copyright">© 2014 Company Name &nbsp;All right reserved &nbsp;Term of Use</div>
</body>
</html>
```